New Business Card Design Project VORALDI-Italy

we are VORALDI-Italy
our company in the market for 3 years we are luxury cosmetic company and its about time for a facelift :)
i will like to have elegant luxurious and unique business card
that will give the person that get it a unique, luxurious and elegant impression
I'm VERY OPEN FOR NEW IDEAS , even duo i add a few files of things that i see on line and i like them

i add my logo as well
my website is VORALDI.COM
(if you would like to see the main style that we have)

Target Market(s)

adult that have money :)

Industry/Entity Type

Business

Contact Information for Business Card

Name - Paul Voraldi
Position - CEO and CO Founder
address - 4718 E Danbury
telephone - 555-318-4402
email - paul@voraldi-example.com
fax - 555-318-4402
website - VORALDI.COM

Colors
000000
959595
fbee3e
ffffff

Requirements
Must have
• big logo in GOLD color
• elegant look
• impressive
Nice to have
• not must but maybe classy pattern background
• not must but maybe emblem
• maybe clear plastic business card
Should not have
• colors
• images

```html
<!DOCTYPE html>
<html lang="en">
<head>
<meta charset="utf-8">
<title>VORALDI Italy — Business Card</title>
<link rel="stylesheet" href="https://fonts.googleapis.com/css2?family=Tinos&family=Titillium+Web:wght@400;600&display=swap">
<style>
  :root {
    --backdrop: #d3d3d7;
    --card: #2a2a2a;
    --gold: #c9a43c;
    --name-grey: #a3a3a6;
    --text-grey: #b4b4b8;
    --divider-dark: #161616;
    --divider-light: #3a3a3a;
  }
  html, body {
    margin: 0;
    width: 1200px;
    height: 1200px;
    overflow: hidden;
    background: var(--backdrop);
  }
  .canvas {
    position: relative;
    width: 1200px;
    height: 1200px;
  }
  .card {
    position: absolute;
    left: 238px;
    width: 724px;
    height: 422px;
    background: var(--card);
    border-radius: 20px;
  }
  .card--front { top: 126px; }
  .card--back  { top: 617px; }

  /* Front */
  .brand-mark {
    position: absolute;
    left: 284px;
    top: 62px;
    width: 148px;
    height: 148px;
  }
  .brand-name {
    position: absolute;
    left: 0;
    right: 0;
    top: 236px;
    margin: 0;
    text-align: center;
    font-family: "Tinos", serif;
    font-weight: 400;
    font-size: 76px;
    line-height: 1;
    letter-spacing: 1px;
    color: var(--gold);
  }
  .brand-rule {
    position: absolute;
    left: 194px;
    top: 312px;
    width: 328px;
    height: 3px;
    background: var(--gold);
  }
  .brand-origin {
    position: absolute;
    left: 0;
    right: 0;
    top: 330px;
    text-align: center;
    font-family: "Tinos", serif;
    font-size: 26px;
    line-height: 1;
    letter-spacing: 1px;
    color: var(--gold);
  }

  /* Back */
  .holder-name {
    position: absolute;
    left: 52px;
    top: 162px;
    margin: 0;
    font-family: "Titillium Web", sans-serif;
    font-weight: 600;
    font-size: 44px;
    line-height: 1;
    color: var(--name-grey);
  }
  .holder-role {
    position: absolute;
    left: 57px;
    top: 218px;
    margin: 0;
    font-family: "Titillium Web", sans-serif;
    font-weight: 400;
    font-size: 26px;
    line-height: 1;
    color: var(--text-grey);
  }
  .contact-divider {
    position: absolute;
    left: 439px;
    top: 67px;
    width: 2px;
    height: 288px;
    background: linear-gradient(to right, var(--divider-dark) 50%, var(--divider-light) 50%);
  }
  .contact-list {
    position: absolute;
    left: 459px;
    top: 0;
    margin: 0;
    padding: 0;
    list-style: none;
    font-family: "Titillium Web", sans-serif;
    font-weight: 400;
    font-size: 20px;
    line-height: 1;
    color: var(--text-grey);
  }
  .contact-list li { position: absolute; white-space: nowrap; }
  .contact-address { top: 91px; }
  .contact-phone   { top: 149px; }
  .contact-email   { top: 203px; }
  .contact-fax     { top: 254px; }
  .contact-web     { top: 309px; }
</style>
</head>
<body>
<main class="canvas">
  <section class="card card--front" aria-label="Card front">
    <svg class="brand-mark" viewBox="0 0 148 148" aria-hidden="true">
      <circle cx="74" cy="74" r="71" fill="none" stroke="var(--gold)" stroke-width="3"/>
    </svg>
    <h1 class="brand-name">VORALDI</h1>
    <div class="brand-rule"></div>
    <div class="brand-origin">ITALY</div>
  </section>

  <section class="card card--back" aria-label="Card back">
    <h2 class="holder-name">PAUL VORALDI</h2>
    <p class="holder-role">CEO and CO Founder</p>
    <div class="contact-divider"></div>
    <ul class="contact-list">
      <li class="contact-address">4718 E Danbury</li>
      <li class="contact-phone">555-318-4402</li>
      <li class="contact-email">paul@voraldi-example.com</li>
      <li class="contact-fax">555-318-4402</li>
      <li class="contact-web">Voraldi . com</li>
    </ul>
  </section>
</main>
</body>
</html>
```